Astrology Web Site in Need of a Clean & Modern Design

Over the past few months we've converted our site to Wordpress. With the content and structure now in place, it's time for a clean, modern design. Our new site must engage visitors, delivering insights and guidance through a well designed UI/UX. We're taking online astrology to the next level! We've sourced hundreds of amazing images and with the eye of a talented designer we can achieve our goals. Our Wordpress developer is ready to convert your design and launch a truly showcase site. Attached are a few examples of what we would like the design to be modeled on. Further details are included in the attached document "Templates to Design for StarlitPathway.net"

Target Market(s)

female

Industry/Entity Type

Online

Number of Pages Required

4 page

Requirements
Must have
• Use real images and not illustrations.
• Use a 12-columns grid system.
• Zodiac signs/icons should be of a single color with no gradients.
Should not have
• crystals balls, fortune tellers etc...dark and heavy backgrounds (ignore current site design and color).

```html
<!DOCTYPE html>
<html lang="en">
<head>
<meta charset="utf-8">
<title>Starlit Astrology – Leo Daily Horoscope</title>
<link rel="stylesheet" href="https://fonts.googleapis.com/css2?family=Open+Sans:wght@400;600;700;800&display=swap">
<style>
:root{
  --sky-top:#4d6396;
  --sky-mid:#7488bb;
  --sky-low:#b3bfdf;
  --coral:#f47352;
  --coral-dark:#e35c3a;
  --coral-light:#f99a7d;
  --gold:#ffd23a;
  --amber:#f2a21f;
  --white:#ffffff;
  --ink:#222222;
  --text:#666666;
  --muted:#888888;
  --panel:#efefef;
  --panel-2:#e4e4e4;
  --line:#d6d6d6;
}
*{box-sizing:border-box;margin:0;padding:0}
html,body{width:734px;height:1200px;overflow:hidden}
body{
  position:relative;
  font-family:"Open Sans",Arial,sans-serif;
  background:linear-gradient(180deg,var(--sky-top) 0%,var(--sky-mid) 45%,var(--sky-low) 100%);
  color:var(--text);
}
.abs{position:absolute}
.moon{left:560px;top:20px;width:240px;height:240px;border-radius:50%;
  background:radial-gradient(circle at 40% 40%,#f4f6fa,#d6dde8 50%,#aab6c9 72%,transparent 74%)}
/* header */
.brand{left:78px;top:24px;font-size:15px;font-weight:600;color:var(--white);letter-spacing:.5px}
.brand .dot{display:inline-block;width:8px;height:8px;background:var(--coral);margin-right:6px;vertical-align:1px}
.nav span{position:absolute;top:31px;font-size:6.2px;font-weight:600;color:var(--white);white-space:nowrap}
.login{left:600px;top:26px;width:54px;height:17px;border-radius:9px;background:var(--coral);color:#fff;
  font-size:6.4px;font-weight:700;text-align:center;line-height:17px;box-shadow:0 2px 0 #b84a2e}
/* zodiac bar */
.zodiac{left:80px;top:64px;width:574px;height:39px;background:var(--coral);display:flex;border-radius:4px 4px 0 0;overflow:hidden}
.sign{flex:1;text-align:center;color:#fff;border-right:1px solid var(--coral-light);padding-top:3px}
.sign:last-child{border-right:0}
.sign .glyph{display:block;font-size:19px;line-height:22px}
.sign .name{font-size:5.3px;display:block}
.sign.active{background:var(--coral-dark)}
/* main panel */
.panel{left:80px;top:103px;width:574px;height:1064px;background:var(--white);border-radius:0 0 4px 4px}
.hero-side{left:99px;top:121px;width:136px;height:230px;background:var(--coral)}
.leo-art{left:108px;top:138px;width:116px;height:128px;border-radius:50% 40% 45% 50%;
  background:radial-gradient(circle at 45% 40%,var(--gold),var(--amber) 70%,transparent 71%)}
.hero-date{left:99px;top:282px;width:136px;text-align:center;color:#fff;font-size:9.5px}
.hero-title{left:108px;top:306px;color:#fff;font-size:14px;font-weight:700}
.hero-title em{font-style:normal;color:var(--gold)}
.hero-photo{left:235px;top:121px;width:401px;height:230px;
  background:
    radial-gradient(ellipse 38% 55% at 62% 42%,#d9a45a,#a8702f 45%,transparent 75%),
    radial-gradient(ellipse 45% 70% at 78% 60%,#6e4519,transparent 70%),
    linear-gradient(90deg,#5b4726,#8a6a35 35%,#6b4a20 70%,#3e2c12)}
.hero-name{left:251px;top:208px;font-size:40px;font-weight:800;color:#fff}
/* daily block */
.daily{left:99px;top:351px;width:537px;height:114px;background:var(--panel)}
.stats{left:537px;top:351px;width:99px;height:114px;background:var(--panel-2);padding:3px 0 0 23px}
.stats h4,.stats p,.stars{display:block;line-height:12.5px;height:12.5px}
.stats h4{font-size:9px;font-weight:600;color:var(--ink)}
.stats p{font-size:6.3px;color:var(--text)}
.stars{color:var(--coral);font-size:9px;letter-spacing:1px}
.tabs{left:99px;top:351px;display:flex;font-size:7.5px;font-weight:600}
.tab{height:22px;line-height:22px;padding:0 13px;color:var(--text);background:#fff;border:1px solid var(--line);border-top:0}
.tab.on{background:var(--panel);color:var(--coral);border:0;padding:0 10px;width:69px}
.daily-date{left:110px;top:379px;font-size:6.5px;color:var(--ink)}
.daily-date b{color:var(--coral);font-weight:400;font-size:8px}
.daily-text{left:111px;top:397px;width:390px;font-size:6.3px;line-height:12.4px;color:var(--text)}
/* three columns */
.col h3{font-size:12.5px;font-weight:700;color:var(--ink)}
.col .img{margin-top:8px;width:163px;height:102px;border:2px solid #fff;outline:1px solid var(--line)}
.col p{margin-top:8px;width:166px;font-size:6.3px;line-height:10.7px}
.btn{display:inline-block;width:57px;height:17px;border-radius:9px;background:var(--coral);color:#fff;
  font-size:6.2px;font-weight:700;text-align:center;line-height:17px;box-shadow:0 2px 0 #c24f31}
.col .btn{margin-top:10px}
.i1{background:linear-gradient(180deg,#1d3a78 0%,#3f6bb5 40%,#6f9a4a 62%,#3f6d25 100%)}
.i2{background:radial-gradient(circle at 50% 50%,#9cc7f2 0%,#3d7fd0 30%,#1b4a93 60%,#0e2a5c 100%)}
.i3{background:linear-gradient(120deg,#e7cdb6,#f5ebe1 45%,#dcc7b4 70%,#c4ae9c)}
/* intro band */
.band{left:80px;top:705px;width:574px;height:114px;background:#f1f1f1}
.intro .ic{width:31px;height:31px;border-radius:50%;border:1.5px solid var(--coral);float:left;margin-right:4px;display:flex;align-items:center;justify-content:center}
.intro h4{font-size:10px;font-weight:700;color:#444;padding-top:6px;line-height:12px}
.intro h5{font-size:9px;font-weight:400;color:#555;line-height:12px}
.intro p{clear:both;padding-top:9px;width:160px;font-size:6.3px;line-height:11px;color:var(--muted)}
/* articles */
.articles{left:99px;top:839px;width:292px;height:167px;background:var(--coral);color:#fff}
.articles h3{position:absolute;left:17px;top:11px;font-size:12.5px;font-weight:700}
.articles .rule{position:absolute;left:0;top:39px;width:292px;height:1px;background:var(--coral-light)}
.articles .lead{position:absolute;left:17px;top:49px;width:260px;font-size:7.3px;line-height:11px}
.heart{position:absolute;left:8px;top:82px;width:98px;height:80px;
  background:radial-gradient(circle at 40% 40%,var(--gold),#f39b2a 75%);border-radius:45% 45% 50% 50%/40% 40% 60% 60%}
.articles .body{position:absolute;left:107px;top:91px;width:172px;font-size:6.3px;line-height:10.3px}
.strip{left:391px;top:839px;width:60px;height:167px;display:flex;flex-direction:column}
.strip div{flex:1;background:var(--coral-light);border-bottom:2px solid #fff;display:flex;align-items:center;justify-content:center}
.strip div:nth-child(2){background:#fbb59c}
.strip div:last-child{border:0}
.promo{left:471px;top:839px;width:165px;height:167px;
  background:
    radial-gradient(circle at 78% 28%,#fdf3df 0%,#f3d9b8 14%,transparent 30%),
    linear-gradient(160deg,#4b5f94,#7b6fa8 55%,#c98fa0)}
.promo .btn{position:absolute;left:9px;top:45px;height:15px;line-height:15px}
.promo .copy{position:absolute;left:12px;top:68px;color:#fff;font-weight:700;line-height:1.05}
.copy .s{font-size:11.5px}
.copy .f{font-size:19px;color:var(--gold)}
.copy .h{font-size:19px}
.copy .q{font-size:11.5px}
/* footer */
.fcol h4{font-size:9px;font-weight:400;color:var(--ink);margin-bottom:14px}
.fcol p{font-size:6.3px;line-height:10px;color:#555}
.field{margin-top:8px;width:135px;height:17px;border:1px solid var(--line);font-size:6.3px;padding:5px 4px;color:#444}
.phone{margin-top:10px;font-size:10px;font-weight:700;color:var(--coral)}
.phone small{font-size:6px}
.mail{font-size:7px;font-weight:600;color:#777}
.social{margin-top:14px;display:flex;gap:3px}
.social span{width:16px;height:16px;border-radius:50%;border:1px solid #bbb}
.links p{font-size:6.3px;line-height:12px;color:#555}
.ideas p{font-size:8.2px;line-height:15.6px;color:var(--ink);padding-left:2px}
.copyright{left:0;top:1179px;width:734px;text-align:center;font-size:6.3px;color:#ffffff}
</style>
</head>
<body>
<div class="abs moon" role="img" aria-label="Soft full moon photograph in the evening sky"></div>

<header>
  <div class="abs brand"><span class="dot"></span>Starlit Astrology</div>
  <nav class="nav">
    <span style="left:277px">HOROSCOPES</span>
    <span style="left:337px">ASTROLOGY</span>
    <span style="left:395px">COMPATIBILITY</span>
    <span style="left:463px">REPORTS</span>
    <span style="left:506px">ABOUT STARLIT ASTROLOGY</span>
  </nav>
  <div class="abs login">LOGIN</div>
</header>

<div class="abs zodiac">
  <div class="sign"><span class="glyph">♈&#xFE0E;</span><span class="name">ARIES</span></div>
  <div class="sign"><span class="glyph">♉&#xFE0E;</span><span class="name">TAURUS</span></div>
  <div class="sign"><span class="glyph">♊&#xFE0E;</span><span class="name">GEMINI</span></div>
  <div class="sign"><span class="glyph">♋&#xFE0E;</span><span class="name">CANCER</span></div>
  <div class="sign active"><span class="glyph">♌&#xFE0E;</span><span class="name">LEO</span></div>
  <div class="sign"><span class="glyph">♍&#xFE0E;</span><span class="name">VIRGO</span></div>
  <div class="sign"><span class="glyph">♎&#xFE0E;</span><span class="name">LIBRA</span></div>
  <div class="sign"><span class="glyph">♏&#xFE0E;</span><span class="name">SCORPIO</span></div>
  <div class="sign"><span class="glyph">♑&#xFE0E;</span><span class="name">CAPRICORN</span></div>
  <div class="sign"><span class="glyph">♐&#xFE0E;</span><span class="name">SAGITTARIUS</span></div>
  <div class="sign"><span class="glyph">♒&#xFE0E;</span><span class="name">AQUARIUS</span></div>
  <div class="sign"><span class="glyph">♓&#xFE0E;</span><span class="name">PISCES</span></div>
</div>

<main>
  <div class="abs panel"></div>

  <div class="abs hero-side"></div>
  <div class="abs leo-art" role="img" aria-label="Golden lion emblem illustration"></div>
  <div class="abs hero-date">Jul 23rd-Aug 22nd</div>
  <div class="abs hero-title">Daily <em>Horoscope</em></div>
  <div class="abs hero-photo" role="img" aria-label="Photograph of a lion with a golden mane in warm sunlight"></div>
  <div class="abs hero-name">Leo</div>

  <div class="abs daily"></div>
  <div class="abs tabs"><div class="tab on">YESTERDAY</div><div class="tab">TODAY</div><div class="tab">TOMORROW</div></div>
  <div class="abs daily-date"><b>Leo</b> February 3rd 2015</div>
  <p class="abs daily-text">It's a great day to pursue something you've been coveting for some time. This might be anything from a job promotion to a new outfit to someone cute and special. Your energy is high and you're feeling courageous, but there's more to it than that. Your natural charisma is really shining now.You're drawing good things your way, simply because you believe you deserve them. It's your very own law of attraction!</p>
  <div class="abs stats">
    <h4>RATING</h4><span class="stars">★★★★★</span>
    <h4>INTENSITY</h4><p>85%</p>
    <h4>KEYWORDS</h4><p>Idealistic, proud</p>
    <h4>MOOD</h4><p>Classy</p>
  </div>

  <section class="abs col" style="left:99px;top:482px">
    <h3>Weekly Horoscope</h3>
    <div class="img i1" role="img" aria-label="Evening sky with a glowing zodiac wheel above green tea fields"></div>
    <p>An intense romantic relationship could heat up nicely. Spending quality time with the object of your affection will extremely enjoyable. If you're single.</p>
    <span class="btn">READ MORE</span>
  </section>
  <section class="abs col" style="left:286px;top:482px">
    <h3>Monthly Horoscope</h3>
    <div class="img i2" role="img" aria-label="Blue zodiac wheel with the twelve signs"></div>
    <p>An intense romantic relationship could heat up nicely. Spending quality time with the object of your affection will extremely enjoyable. If you're single.</p>
    <span class="btn">READ MORE</span>
  </section>
  <section class="abs col" style="left:471px;top:482px">
    <h3>Yearly Horoscope</h3>
    <div class="img i3" role="img" aria-label="Two women smiling at a soft light in cupped hands"></div>
    <p>An intense romantic relationship could heat up nicely. Spending quality time with the object of your affection will extremely enjoyable. If you're single.</p>
    <span class="btn">READ MORE</span>
  </section>

  <div class="abs band"></div>
  <section class="abs intro" style="left:99px;top:726px">
    <div class="ic"><svg width="12" height="12" viewBox="0 0 24 24"><path fill="#f47352" d="M12 2l3 7h7l-5.5 4.5 2 7.5L12 16.5 5.5 21l2-7.5L2 9h7z"/></svg></div>
    <h4>STARLIT ASTROLOGY</h4><h5>Introduction</h5>
    <p>Lorem ipsum dolor sit amet, consectetur adipiscing elit, sed do eiusmod tempor incididunt ut labore et dolore magna aliqua. Ut enim ad minim .</p>
  </section>
  <section class="abs intro" style="left:289px;top:726px">
    <div class="ic"><svg width="13" height="12" viewBox="0 0 24 22"><path fill="#f47352" d="M12 21L2 11A6 6 0 0112 4a6 6 0 0110 7z"/></svg></div>
    <h4>LOVE AND ROMANCE</h4><h5>Introduction</h5>
    <p>Lorem ipsum dolor sit amet, consectetur adipiscing elit, sed do eiusmod tempor incididunt ut labore et dolore magna aliqua. Ut enim ad minim .</p>
  </section>
  <section class="abs intro" style="left:476px;top:726px">
    <div class="ic"><svg width="12" height="14" viewBox="0 0 24 28"><g fill="#f47352"><circle cx="7" cy="4" r="3"/><circle cx="17" cy="4" r="3"/><rect x="4" y="8" width="6" height="19" rx="2"/><rect x="14" y="8" width="6" height="19" rx="2"/></g></svg></div>
    <h4>FRIENDS AND FAMILY</h4><h5>Introduction</h5>
    <p>Lorem ipsum dolor sit amet, consectetur adipiscing elit, sed do eiusmod tempor incididunt ut labore et dolore magna aliqua. Ut enim ad minim .</p>
  </section>

  <section class="abs articles">
    <h3>LEO Articles</h3>
    <div class="rule"></div>
    <p class="lead">Lorem ipsum dolor sit amet, consectetur adipiscing elit, sed do eiusmod tempor incididunt ut labore et dolore magna aliqua.</p>
    <div class="heart" role="img" aria-label="Golden heart with the Leo sign"></div>
    <p class="body">Lorem ipsum dolor sit amet, consectetur adipiscing elit, sed do eiusmod tempor incididunt ut labore et dolore magna aliqua. Ut enim ad minimLorem ipsum dolor sit amet, consectetur adipiscing elit, sed do eiusmod tempor incididunt ut labore et dolore magna aliqua. Ut enim ad minim .</p>
  </section>
  <div class="abs strip">
    <div><svg width="30" height="22" viewBox="0 0 30 22"><g fill="none" stroke="#f2a21f" stroke-width="3"><circle cx="11" cy="12" r="8"/><circle cx="19" cy="12" r="8"/></g></svg></div>
    <div><svg width="30" height="26" viewBox="0 0 30 26"><g fill="#f2a21f"><path d="M3 2h10l-2 9a3 3 0 01-6 0z"/><path d="M17 2h10l-2 9a3 3 0 01-6 0z"/><rect x="7" y="13" width="2" height="9"/><rect x="21" y="13" width="2" height="9"/></g></svg></div>
    <div><svg width="22" height="26" viewBox="0 0 22 26"><path fill="#f2a21f" d="M11 1c3 6 9 9 9 15a9 9 0 01-18 0c0-4 3-6 4-9 1 3 3 4 3 4 0-4 1-7 2-10z"/></svg></div>
  </div>

  <aside class="abs promo" role="img" aria-label="Photograph of a hand reaching toward a rising moon in a twilight sky">
    <span class="btn">SIGN UP</span>
    <div class="copy"><div class="s">Ask your</div><div class="f">FREE</div><div class="h">Horoscope</div><div class="q">Question!</div></div>
  </aside>
</main>

<footer>
  <section class="abs fcol" style="left:99px;top:1049px">
    <h4>Sign Up Newsletter</h4>
    <p>Neque porro quisquam est qui dolorem<br>ipsum quia dolor sit amet.</p>
    <div class="field">Email:</div>
    <span class="btn" style="margin-top:10px">SIGN UP</span>
  </section>
  <section class="abs fcol" style="left:278px;top:1049px">
    <h4>Questions Or Assistance?</h4>
    <p>Feel free to contact us at:</p>
    <div class="phone">1-800-555-0142 <small>or</small></div>
    <div class="mail">hello@starlitpathway.net</div>
    <div class="social"><span></span><span></span><span></span><span></span><span></span></div>
  </section>
  <section class="abs fcol links" style="left:438px;top:1049px">
    <h4>Quick Links</h4>
    <p>NEW! ASK a Free Question</p><p>2015 Horoscope</p><p>2015 Chinese Forecasts</p><p>Find Your Perfect Match!</p><p>Free Horoscope Newsletter</p><p>Free Daily Tarot</p>
  </section>
  <section class="abs fcol ideas" style="left:552px;top:1049px">
    <h4>Hot Date Ideas</h4>
    <p style="margin-top:-12px">Love Lies You're</p><p>Dating Deal Breakers</p><p>Mayan Astrology 101</p><p>Signs He's Over You</p>
  </section>
  <div class="abs copyright">© 2015. All Rights Reserved. Starlit Astrology</div>
</footer>
</body>
</html>
```